Delcourt Realty Business Cards

Design business card

Target Market(s)

High-End Buyer of Real Estate over $1 million dollars

Industry/Entity Type

Realtor

Contact Information for Business Card

Lena Delcourt R(S) LIC.# 41972
Cell 555 246-1938
Email Lena@Delcourt.example
Website IsleFreshHomes.example

Also Need Cards for:

Hank Delcourt R(B) LIC# 69418
C 555 613-7052
E Hank@Delcourt.example
W IsleFreshHomes.example

Colors

Designer to choose colors to be used in the design.

Requirements
Must have
• Address on back:
• 287 Pohaku Cir. , Wailea HI 96753
• Logo on back
Nice to have
• I would like the phone numbers and email address to be big so people can read it easily
Should not have
• Very small print Except For: address (287 Pohaku Cir. Wailea HI 96753)

```html
<!DOCTYPE html>
<html lang="en">
<head>
<meta charset="utf-8">
<title>Delcourt Realty Business Cards</title>
<link href="https://fonts.googleapis.com/css2?family=Montserrat:wght@400;500;600;700&display=swap" rel="stylesheet">
<style>
  :root {
    --navy: #0f2843;
    --sky: #5ecbea;
    --white: #ffffff;
    --page: #ffffff;
    --label: #1a1a1a;
    --shadow: rgba(0, 0, 0, 0.45);
  }
  * { box-sizing: border-box; margin: 0; padding: 0; }
  html, body { width: 1200px; height: 1000px; overflow: hidden; background: var(--page); }
  body { position: relative; font-family: "Montserrat", Arial, sans-serif; color: var(--navy); }

  .card {
    position: absolute;
    width: 489px;
    height: 281px;
    box-shadow: 5px 5px 7px var(--shadow);
    overflow: hidden;
  }
  .card--front { background: var(--white); top: 187px; }
  .card--lena { left: 97px; }
  .card--hank { left: 620px; }
  .card--back { background: var(--navy); left: 350px; top: 542px; }

  .side-label {
    position: absolute;
    width: 489px;
    text-align: center;
    font-size: 13px;
    font-weight: 500;
    color: var(--label);
    letter-spacing: 0.5px;
  }
  .side-label--lena { left: 97px; top: 486px; }
  .side-label--hank { left: 620px; top: 486px; }
  .side-label--back { left: 350px; top: 844px; }

  .brand-row { position: absolute; left: 112px; top: 36px; display: flex; align-items: flex-end; }
  .brand-box {
    width: 190px; height: 63px;
    background: var(--navy);
    border-radius: 8px;
    display: flex; flex-direction: column; justify-content: center; align-items: center;
    color: var(--white);
    font-weight: 600;
    font-size: 20px;
    line-height: 1.1;
    letter-spacing: 2px;
  }
  .agent-photo { width: 82px; height: 62px; }

  .agent-name {
    position: absolute; left: 0; right: 0; top: 116px;
    text-align: center;
    font-size: 30px; font-weight: 700; letter-spacing: 0.5px;
  }
  .agent-license {
    position: absolute; left: 0; right: 0; top: 153px;
    text-align: center;
    font-size: 13px; font-weight: 400; letter-spacing: 2px;
  }
  .contact-list { position: absolute; left: 123px; top: 180px; list-style: none; }
  .contact-item { display: flex; align-items: center; height: 28px; font-size: 20px; font-weight: 600; }
  .contact-tag {
    width: 14px; height: 14px; margin-right: 7px;
    background: var(--sky); border-radius: 2px;
    color: var(--white); font-size: 8px; font-weight: 700;
    display: flex; align-items: center; justify-content: center;
  }
  .web-band {
    position: absolute; left: 0; right: 0; bottom: 0; height: 28px;
    background: var(--sky);
    color: var(--white);
    font-size: 11px; font-weight: 600; letter-spacing: 4.5px;
    display: flex; align-items: center; justify-content: center;
  }

  .back-brand {
    position: absolute; left: 65px; top: 96px; width: 361px; height: 54px;
    background: var(--white); border-radius: 9px;
    display: flex; align-items: center; justify-content: center;
    font-size: 30px; font-weight: 600; letter-spacing: 1px; color: var(--navy);
  }
  .back-address {
    position: absolute; left: 0; right: 0; top: 170px;
    text-align: center;
    color: var(--white);
    font-size: 15px; font-weight: 600; letter-spacing: 3px;
  }
  .back-address .dot { color: var(--sky); }
</style>
</head>
<body>

  <section class="card card--front card--lena">
    <div class="brand-row">
      <div class="brand-box"><span>DELCOURT</span><span>REALTY</span></div>
      <svg class="agent-photo" role="img" aria-label="Portrait photo of the two agents" viewBox="0 0 82 62">
        <defs>
          <linearGradient id="photoTone1" x1="0" y1="0" x2="1" y2="0">
            <stop offset="0" stop-color="#e7b7a6"/>
            <stop offset="0.45" stop-color="#e14f86"/>
            <stop offset="1" stop-color="#1d1d24"/>
          </linearGradient>
        </defs>
        <rect width="82" height="62" fill="url(#photoTone1)"/>
      </svg>
    </div>
    <h1 class="agent-name">LENA DELCOURT R(S)</h1>
    <p class="agent-license">LIC.# 41972</p>
    <ul class="contact-list">
      <li class="contact-item"><span class="contact-tag">c.</span>555.246.1938</li>
      <li class="contact-item"><span class="contact-tag">e.</span>LENA@DELCOURT.EXAMPLE</li>
    </ul>
    <div class="web-band">ISLEFRESHHOMES.EXAMPLE</div>
  </section>
  <p class="side-label side-label--lena">FRONT</p>

  <section class="card card--front card--hank">
    <div class="brand-row">
      <div class="brand-box"><span>DELCOURT</span><span>REALTY</span></div>
      <svg class="agent-photo" role="img" aria-label="Portrait photo of the two agents" viewBox="0 0 82 62">
        <defs>
          <linearGradient id="photoTone2" x1="0" y1="0" x2="1" y2="0">
            <stop offset="0" stop-color="#e7b7a6"/>
            <stop offset="0.45" stop-color="#e14f86"/>
            <stop offset="1" stop-color="#1d1d24"/>
          </linearGradient>
        </defs>
        <rect width="82" height="62" fill="url(#photoTone2)"/>
      </svg>
    </div>
    <h1 class="agent-name">HANK DELCOURT R(B)</h1>
    <p class="agent-license">LIC.# 69418</p>
    <ul class="contact-list">
      <li class="contact-item"><span class="contact-tag">c.</span>555.613.7052</li>
      <li class="contact-item"><span class="contact-tag">e.</span>HANK@DELCOURT.EXAMPLE</li>
    </ul>
    <div class="web-band">ISLEFRESHHOMES.EXAMPLE</div>
  </section>
  <p class="side-label side-label--hank">FRONT</p>

  <section class="card card--back">
    <div class="back-brand">DELCOURT REALTY</div>
    <p class="back-address">287 POHAKU CIR. <span class="dot">•</span> WAILEA HI 96753</p>
  </section>
  <p class="side-label side-label--back">BACK</p>

</body>
</html>
```